Young judge needs a website to publish and to connect

I would like to have a website where I can publish my articles in public law. I am judge at the Alpine Civic Review Tribunal. Therefore, the website must have a calm, friendly and fairly neutral design. Also, it should be mobile friendly and easy to use.

On my website, I want to

- publish articles such as https://www.brindlepost.example/pulse/how-win-court-tobias-wenger/ and get feedbacks from my colleagues
- generate interest for my project on 'Statutes and Society - Notes from the Chamber', a book that I would like to publish in 2020 and which brings together my publications on public law (http://www.civicnorm.example/content/english/profil/publikationen.html ).
- provide updates for my university courses on constitutional, administrative and international law.

For that purpose, I would kindly ask you to suggest a website that communicates a fresh approach to the work of a young judge in constitutional and administrative law. Please have in mind that I do not only sit on the bench, but that I also work in academia. Therefore, it should be suitable for an audience from both university and law practice. The website should replace the existing website on www.civicnorm.example that I designed when still working as a lawyer. Thank you.

Target Market(s)

Academica, law firms, courts

Industry/Entity Type

University

Contact Information for Business Card

Tobias Wenger
Judge
Alpine Civic Review Tribunal
M +41 79 5XX 8X 2X

Logo Text

Notes from the Chamber

Number of Pages Required

5+ page

Font styles to use
Sans Serif

Colors
0455a3

Requirements
Must have
• - a page where I can publish and get feedbacks
• - a page about my project on law and politics
• - a page where I can provide updates for my university courses on constitutional, administrative and international law
• - page where I can list current and planned projects
• - a collaborative, young and fresh approach
Nice to have
• - a page reserved for my colleagues at the Alpine Civic Review Tribunal where I can alert them about to possibility to collaborate (if possibly password protected) and where they may suggest what to contribute to a specific project
Should not have
• anything which might to suggest that I want to make money with it, bragging or pretentious. Do not forget: I am judge, not a barrister.

```html
<!DOCTYPE html>
<html lang="en">
<head>
<meta charset="utf-8">
<title>Projects – Tobias Wenger</title>
<link rel="stylesheet" href="https://fonts.googleapis.com/css2?family=Montserrat:wght@500;600;700&family=Nunito+Sans:wght@400;600;700;800&display=swap">
<style>
  :root {
    --brand-blue: #0455a3;
    --accent-gold: #f2b705;
    --ink: #3a3f45;
    --ink-soft: #55595e;
    --card-bg: #f2f2f2;
    --card-shadow: rgba(0,0,0,0.18);
    --inactive-bg: #aaaaaa;
    --white: #ffffff;
    --search-bg: #eef1f5;
    --search-border: #b9c6d8;
    --status-blue: #0d4a94;
    --icon-dark: #2b3238;
  }
  * { box-sizing: border-box; margin: 0; padding: 0; }
  html, body { width: 1200px; height: 775px; overflow: hidden; background: var(--white); }
  body { position: relative; font-family: "Nunito Sans", Arial, sans-serif; color: var(--ink); }

  .site-header { position: absolute; left: 0; top: 0; width: 1200px; height: 110px; background: var(--brand-blue); color: var(--white); }
  .brand { position: absolute; left: 0; width: 1200px; top: 21px; text-align: center; }
  .brand-name { font-family: "Montserrat", sans-serif; font-weight: 600; font-size: 23px; letter-spacing: 3.6px; line-height: 26px; padding-left: 3.6px; }
  .brand-tagline { font-family: "Montserrat", sans-serif; font-weight: 500; font-size: 12px; letter-spacing: 9.6px; margin-top: 4px; padding-left: 9.6px; }

  .main-nav { position: absolute; top: 87px; left: 0; width: 1200px; height: 18px; }
  .nav-item { position: absolute; top: 0; transform: translateX(-50%); font-family: "Montserrat", sans-serif; font-weight: 600; font-size: 13px; line-height: 18px; color: var(--white); text-decoration: none; white-space: nowrap; }
  .nav-sep { position: absolute; top: 5px; width: 2px; height: 9px; background: var(--accent-gold); }
  .nav-home { position: absolute; left: 321px; top: 1px; }

  .page-title { position: absolute; left: 318px; top: 150px; font-family: "Montserrat", sans-serif; font-weight: 600; font-size: 30px; line-height: 34px; letter-spacing: 3.6px; color: var(--ink); }

  .view-option { position: absolute; left: 320px; display: flex; align-items: center; gap: 9px; font-size: 10px; font-weight: 600; letter-spacing: 0.9px; color: var(--ink); }
  .view-option svg { display: block; }

  .search { position: absolute; left: 320px; top: 303px; width: 125px; height: 22px; border: 1px solid var(--search-border); border-radius: 3px; background: var(--search-bg); display: flex; align-items: center; padding-left: 9px; gap: 7px; font-size: 9.5px; color: #6a7380; letter-spacing: 0.4px; }

  .filters { position: absolute; left: 322px; top: 355px; }
  .filters h2 { font-weight: 600; font-size: 14px; letter-spacing: 1.5px; color: var(--ink); margin-bottom: 10px; }
  .filters li { list-style: none; font-size: 9.8px; letter-spacing: 0.8px; line-height: 18px; color: var(--ink); font-weight: 600; }
  .filters li b { font-weight: 800; }

  .project-card { position: absolute; width: 163px; height: 162px; background: var(--card-bg); box-shadow: 0 1px 2px var(--card-shadow); }
  .project-card .thumb { width: 163px; height: 109px; }
  .project-card .info { position: absolute; left: 7px; top: 109px; width: 149px; }
  .project-name, .project-client { font-size: 11px; font-weight: 600; letter-spacing: 1.1px; color: var(--ink-soft); line-height: 17.5px; }
  .project-name { margin-top: 2px; }
  .project-status { position: absolute; right: 9px; bottom: 5px; font-size: 8px; font-weight: 600; letter-spacing: 0.9px; color: var(--status-blue); }
  .placeholder { display: flex; align-items: center; justify-content: center; }

  .project-card.inactive { background: var(--inactive-bg); }
  .project-card.inactive .project-name,
  .project-card.inactive .project-client,
  .project-card.inactive .project-status { color: var(--white); }

  .thumb-glass { background: linear-gradient(160deg, #8fb4dc 0%, #3d74b4 40%, #1c4b86 100%); }
  .thumb-columns { background: linear-gradient(180deg, #9a9894 0%, #5b5752 45%, #2a2725 100%); }
  .thumb-books { background: linear-gradient(135deg, #c9a894 0%, #b18470 45%, #8d5d4b 100%); }
  .thumb-shelf { background: radial-gradient(circle at 55% 60%, #b07a3a 0%, #5a2b14 45%, #241008 100%); }
</style>
</head>
<body>
  <header class="site-header">
    <div class="brand">
      <div class="brand-name">TOBIAS WENGER</div>
      <div class="brand-tagline">EXPERTISE IN LAW</div>
    </div>
    <nav class="main-nav">
      <a class="nav-home" href="#" aria-label="Home">
        <svg width="19" height="16" viewBox="0 0 19 16"><path d="M9.5 0 L19 8 H16 V16 H3 V8 H0 Z" fill="#ffffff"/></svg>
      </a>
      <a class="nav-item" href="#" style="left:412px">Articles</a>
      <span class="nav-sep" style="left:484px"></span>
      <a class="nav-item" href="#" style="left:558px">Law and Politics</a>
      <span class="nav-sep" style="left:631px"></span>
      <a class="nav-item" href="#" style="left:706px">University</a>
      <span class="nav-sep" style="left:778px"></span>
      <a class="nav-item" href="#" style="left:853px">Projects</a>
    </nav>
  </header>

  <h1 class="page-title">Projects</h1>

  <div class="view-option" style="top:232px">
    <svg width="13" height="13" viewBox="0 0 13 13" fill="#0455a3">
      <rect x="0" y="0" width="3" height="3"/><rect x="5" y="0" width="3" height="3"/><rect x="10" y="0" width="3" height="3"/>
      <rect x="0" y="5" width="3" height="3"/><rect x="5" y="5" width="3" height="3"/><rect x="10" y="5" width="3" height="3"/>
      <rect x="0" y="10" width="3" height="3"/><rect x="5" y="10" width="3" height="3"/><rect x="10" y="10" width="3" height="3"/>
    </svg>
    Grid View
  </div>
  <div class="view-option" style="top:261px">
    <svg width="14" height="13" viewBox="0 0 14 13" fill="#0455a3">
      <rect x="0" y="0" width="2" height="2"/><rect x="4" y="0" width="10" height="2"/>
      <rect x="0" y="3.7" width="2" height="2"/><rect x="4" y="3.7" width="10" height="2"/>
      <rect x="0" y="7.4" width="2" height="2"/><rect x="4" y="7.4" width="10" height="2"/>
      <rect x="0" y="11" width="2" height="2"/><rect x="4" y="11" width="10" height="2"/>
    </svg>
    List View
  </div>

  <div class="search">
    <svg width="10" height="10" viewBox="0 0 10 10" fill="none" stroke="#5f6b7a" stroke-width="1.3"><circle cx="4.2" cy="4.2" r="3.3"/><path d="M6.7 6.7 L9.3 9.3"/></svg>
    Search
  </div>

  <section class="filters">
    <h2>Show</h2>
    <ul>
      <li>Everything : <b>All</b></li>
      <li>Project State : <b>All</b></li>
      <li>Project Type : <b>All</b></li>
      <li>Client : <b>All</b></li>
      <li>Tag : <b>All</b></li>
    </ul>
  </section>

  <article class="project-card" style="left:514px; top:155px">
    <div class="thumb thumb-glass" role="img" aria-label="Photo of a glass office tower against a blue sky"></div>
    <div class="info"><p class="project-name">Project Name</p><p class="project-client">Client</p></div>
    <span class="project-status">ACTIVE</span>
  </article>

  <article class="project-card" style="left:717px; top:155px">
    <div class="thumb thumb-columns" role="img" aria-label="Photo of stone columns of a classical courthouse under a cloudy sky"></div>
    <div class="info"><p class="project-name">Project Name</p><p class="project-client">Client</p></div>
    <span class="project-status">ACTIVE</span>
  </article>

  <article class="project-card" style="left:514px; top:357px">
    <div class="thumb thumb-books" role="img" aria-label="Photo of many open books laid out side by side"></div>
    <div class="info"><p class="project-name">Project Name</p><p class="project-client">Client</p></div>
    <span class="project-status">ACTIVE</span>
  </article>

  <article class="project-card inactive" style="left:717px; top:357px">
    <div class="thumb placeholder">
      <svg width="56" height="48" viewBox="0 0 56 48"><rect x="2" y="2" width="52" height="44" rx="3" fill="none" stroke="#ffffff" stroke-width="4"/><circle cx="15" cy="15" r="5" fill="#ffffff"/><path d="M8 40 L20 24 L28 32 L38 18 L50 40 Z" fill="#ffffff"/></svg>
    </div>
    <div class="info"><p class="project-name">Project Name</p><p class="project-client">Client</p></div>
    <span class="project-status">INACTIVE</span>
  </article>

  <article class="project-card" style="left:514px; top:558px">
    <div class="thumb placeholder">
      <svg width="56" height="48" viewBox="0 0 56 48"><rect x="2" y="2" width="52" height="44" rx="3" fill="none" stroke="#2b3238" stroke-width="4"/><circle cx="15" cy="15" r="5" fill="#2b3238"/><path d="M8 40 L20 24 L28 32 L38 18 L50 40 Z" fill="#2b3238"/></svg>
    </div>
    <div class="info"><p class="project-name">Project Name</p><p class="project-client">Client</p></div>
    <span class="project-status">ACTIVE</span>
  </article>

  <article class="project-card" style="left:717px; top:558px">
    <div class="thumb thumb-shelf" role="img" aria-label="Photo of old leather-bound books on a warmly lit wooden shelf"></div>
    <div class="info"><p class="project-name">Project Name</p><p class="project-client">Client</p></div>
    <span class="project-status">ACTIVE</span>
  </article>
</body>
</html>
```